Corvane Capital LLC
I need single sided standard sized Business Card [3.5" x 2"]
Fonts to be determined by designer
Professional
Derek Halloway
Chairman
Kestrel Hall Tower
418 North Larkin Avenue
Los Angeles, CA 90099
555.014.2739 X1
Acquisitions@Corvane-Capital.net
http://www.Corvane-Capital.net
We want to see what designs are out there for a cutting edge business card that shows off our 3 main goals: Intense - Expressive - Important . The business card can be vertical or horizontal, can use fonts of the designer's choice and be relatively "unique". More than just a simple black on white business card.
Use the logo and CORVANE but you do not need to use the blue background if your design does not warrant it. Financial LLC can be in any font you desire if it matches your design

```html
<!DOCTYPE html>
<html lang="en">
<head>
<meta charset="utf-8">
<title>Corvane Capital LLC — Stationery</title>
<link href="https://fonts.googleapis.com/css2?family=Lato:wght@400;700&display=swap" rel="stylesheet">
<style>
  :root {
    --bg: #e9e6e2;
    --paper: #ffffff;
    --ink: #2a2a2a;
    --muted: #6b6b6b;
    --black: #141414;
    --gold: #b08a3e;
    --gold-light: #d8b66a;
    --gold-dark: #7a5a1e;
    --faint: #ebebeb;
  }
  * { margin: 0; padding: 0; box-sizing: border-box; }
  html, body { width: 1200px; height: 497px; overflow: hidden; }
  body {
    background: var(--bg);
    font-family: "Lato", sans-serif;
    color: var(--ink);
    position: relative;
  }
  .piece { position: absolute; background: var(--paper); box-shadow: 0 2px 6px rgba(0,0,0,.2); overflow: hidden; }
  .brand { font-weight: 700; color: var(--gold); letter-spacing: .08em; white-space: nowrap; line-height: 1; }
  .sub { font-weight: 400; color: var(--muted); white-space: nowrap; line-height: 1; }
  .lines { white-space: nowrap; }
  .gold-bar { position: absolute; width: 7px; background: linear-gradient(180deg, var(--gold-light), var(--gold-dark)); }
  .watermark { position: absolute; font-weight: 700; color: var(--faint); letter-spacing: .08em; white-space: nowrap; line-height: 1; }

  /* Business card front */
  .card-front { left: 17px; top: 70px; width: 194px; height: 115px; }
  .card-front .logo { position: absolute; left: 12px; top: 50px; }
  .card-front .logo .brand { font-size: 15px; }
  .card-front .logo .sub { font-size: 5px; letter-spacing: .42em; margin-top: 3px; }
  .card-front .person { position: absolute; left: 92px; top: 16px; font-size: 7px; line-height: 1.35; }
  .card-front .person strong { display: block; font-weight: 700; }
  .card-front .contact { position: absolute; left: 92px; top: 44px; font-size: 5.2px; line-height: 1.55; }
  .card-front .gold-bar { right: 0; top: 44px; height: 30px; }

  /* Business card back */
  .card-back { left: 218px; top: 70px; width: 194px; height: 115px; background: var(--black); color: #e6e6e6; }
  .card-back .gold-bar { left: 0; top: 44px; height: 30px; }
  .card-back .logo { position: absolute; left: 18px; top: 20px; }
  .card-back .logo .brand { font-size: 11px; }
  .card-back .logo .sub { font-size: 4px; letter-spacing: .42em; margin-top: 2px; color: #a9a9a9; }
  .card-back .person { position: absolute; left: 96px; top: 16px; font-size: 7px; line-height: 1.35; }
  .card-back .person strong { display: block; font-weight: 700; }
  .card-back .contact { position: absolute; left: 96px; top: 44px; font-size: 5.2px; line-height: 1.55; color: #cfcfcf; }
  .card-back .url { position: absolute; left: 0; right: 0; bottom: 8px; text-align: center; font-size: 5px; color: var(--gold-light); }

  /* Letterhead */
  .letterhead { left: 437px; top: 29px; width: 182px; height: 259px; }
  .letterhead .logo { position: absolute; left: 12px; top: 14px; }
  .letterhead .logo .brand { font-size: 9px; }
  .letterhead .sender { position: absolute; left: 108px; top: 12px; font-size: 3.8px; line-height: 1.5; color: var(--muted); }
  .letterhead .watermark { left: 30px; top: 150px; font-size: 22px; }

  /* Envelope back (dark flap) */
  .env-back { left: 806px; top: 26px; width: 365px; height: 128px; }
  .env-back .flap { position: absolute; inset: 0; }
  .env-back .seal { position: absolute; left: 0; right: 0; top: 22px; text-align: center; }
  .env-back .seal .brand { font-size: 9px; }

  /* Envelope middle */
  .env-mid { left: 782px; top: 130px; width: 389px; height: 129px; }
  .env-mid .watermark { right: 20px; bottom: 14px; font-size: 15px; }

  /* Envelope front (gold flap) */
  .env-front { left: 665px; top: 202px; width: 384px; height: 268px; }
  .env-front .flap { position: absolute; left: 0; top: 0; width: 100%; height: 70px; }
  .env-front .logo { position: absolute; left: 0; right: 0; top: 100px; text-align: center; }
  .env-front .logo .brand { font-size: 26px; }
  .env-front .logo .sub { font-size: 6px; letter-spacing: .5em; margin-top: 5px; }
  .env-front .sender { position: absolute; left: 14px; top: 178px; font-size: 4.6px; line-height: 1.55; color: var(--muted); }
  .env-front .watermark { right: 18px; bottom: 16px; font-size: 18px; }
</style>
</head>
<body>

  <section class="piece card-front" aria-label="Business card front">
    <div class="logo">
      <div class="brand">CORVANE</div>
      <div class="sub">CAPITAL</div>
    </div>
    <div class="person"><strong>Derek Halloway</strong>Chairman</div>
    <div class="contact lines">
      Kestrel Hall Tower<br>418 North Larkin Avenue<br>Los Angeles, CA 90099<br>555.014.2739 X1<br>Acquisitions@Corvane-Capital.net<br>http://www.Corvane-Capital.net
    </div>
    <div class="gold-bar"></div>
  </section>

  <section class="piece card-back" aria-label="Business card back">
    <div class="gold-bar"></div>
    <div class="logo">
      <div class="brand">CORVANE</div>
      <div class="sub">CAPITAL</div>
    </div>
    <div class="person"><strong>Derek Halloway</strong>Chairman</div>
    <div class="contact lines">
      Kestrel Hall Tower<br>418 North Larkin Avenue<br>Los Angeles, CA 90099<br>555.014.2739 X1<br>Acquisitions@Corvane-Capital.net
    </div>
    <div class="url">http://www.Corvane-Capital.net</div>
  </section>

  <section class="piece letterhead" aria-label="Letterhead">
    <div class="logo"><span class="brand">CORVANE</span></div>
    <div class="sender lines">
      Kestrel Hall Tower<br>418 North Larkin Avenue<br>Los Angeles, CA 90099<br>555.014.2739 X1<br>Acquisitions@Corvane-Capital.net<br>http://www.Corvane-Capital.net
    </div>
    <div class="watermark">CORVANE</div>
  </section>

  <section class="piece env-back" aria-label="Envelope back">
    <svg class="flap" viewBox="0 0 365 128" preserveAspectRatio="none">
      <polygon points="0,0 365,0 182,76" fill="#141414"/>
      <polyline points="0,128 182,66 365,128" fill="none" stroke="#dcdcdc" stroke-width="1"/>
    </svg>
    <div class="seal"><span class="brand">CORVANE</span></div>
  </section>

  <section class="piece env-mid" aria-label="Envelope">
    <div class="watermark">CORVANE</div>
  </section>

  <section class="piece env-front" aria-label="Envelope front">
    <svg class="flap" viewBox="0 0 384 70" preserveAspectRatio="none">
      <defs>
        <linearGradient id="flapGold" x1="0" y1="0" x2="1" y2="1">
          <stop offset="0" stop-color="#d8b66a"/>
          <stop offset="1" stop-color="#7a5a1e"/>
        </linearGradient>
      </defs>
      <polygon points="0,0 384,0 384,36 192,70 0,36" fill="url(#flapGold)"/>
    </svg>
    <div class="logo">
      <div class="brand">CORVANE</div>
      <div class="sub">CAPITAL</div>
    </div>
    <div class="sender lines">
      Kestrel Hall Tower<br>418 North Larkin Avenue<br>Los Angeles, CA 90099<br>555.014.2739 X1<br>http://www.Corvane-Capital.net
    </div>
    <div class="watermark">CORVANE</div>
  </section>

</body>
</html>
```